Sunwellflow Aquadeepflow Depot

Need a brochure to send to new prospective clients, giving them an idea of what we are and what we can do for them.
To be sent as an attachment to an email.
Printable if possible to hand out at Pastoral Expo Week.
http://www.sunwellflow.com.au/
http://www.aquadeepflow.com.au/
http://www.wellflowy.net.au/
All three of these site are part of what I do.

Target Market(s)

Rural, Sheep and cattle stations, water bore users, out of city living.

Colors
0255a3
0692cd

Requirements
Must have
• Print and email version

```html
<!DOCTYPE html>
<html lang="en">
<head>
<meta charset="utf-8">
<title>Sunwellflow – Submersible Pump How To Guides</title>
<link rel="stylesheet" href="https://fonts.googleapis.com/css2?family=Ubuntu:wght@700&family=Oswald:wght@700&family=Roboto+Condensed:wght@700&family=Open+Sans:ital,wght@0,400;0,600;1,400;1,600&display=swap">
<style>
  :root {
    --navy: #1e3a8a;
    --brand-deep: #0255a3;
    --brand-sky: #0692cd;
    --sun: #f9b51a;
    --sun-light: #fdd63c;
    --orange: #f39a1e;
    --ink: #1b1b1b;
    --muted: #444;
    --paper: #ffffff;
    --paper-shade: #eeeeef;
    --stage: #e4e5e7;
  }
  * { box-sizing: border-box; margin: 0; padding: 0; }
  html, body { width: 1200px; height: 830px; overflow: hidden; background: var(--stage); }
  .canvas { position: relative; width: 1200px; height: 830px; }

  .page { position: absolute; top: 50px; width: 522px; height: 731px; overflow: hidden; background: var(--paper); box-shadow: 0 4px 14px rgba(0,0,0,.18); }
  .page--cover { left: 42px; }
  .page--guide { left: 640px; background: linear-gradient(90deg, var(--brand-deep) 0%, var(--brand-sky) 12%, var(--brand-sky) 88%, var(--brand-deep) 100%); }

  .waves { position: absolute; inset: 0; width: 522px; height: 731px; }

  /* Cover */
  .cover__sun { position: absolute; left: 0; top: 0; width: 522px; height: 260px; background: radial-gradient(circle at 92% 4%, #fff6c9 0%, var(--sun-light) 22%, var(--sun) 70%); }
  .cover__photo { position: absolute; left: 0; top: 170px; width: 522px; height: 430px; background: linear-gradient(170deg, #5fa6de 0%, #a9d2f0 45%, #1e3f86 62%, #2c4f94 80%, #9bcf6a 100%); }
  .cover__title { position: absolute; left: 0; width: 522px; text-align: center; }
  .cover__title--sub { top: 36px; font-family: "Ubuntu", sans-serif; font-size: 43px; color: var(--navy); letter-spacing: .5px; }
  .cover__title--main { top: 84px; font-family: "Oswald", sans-serif; font-size: 62px; line-height: 1; color: #fff; letter-spacing: 1px; text-shadow: 0 2px 0 #9a9a9a, 0 4px 6px rgba(0,0,0,.35); padding-left: 14px; }

  .brand-box { position: absolute; left: 35px; top: 633px; width: 453px; height: 64px; border: 2px solid var(--orange); border-radius: 10px; background: #fff; display: flex; align-items: center; justify-content: space-around; }
  .brand { display: flex; align-items: center; gap: 5px; font-family: "Roboto Condensed", sans-serif; font-weight: 700; font-size: 16px; }
  .brand__dot { width: 9px; height: 9px; border-radius: 50%; background: currentColor; }
  .brand--sun { color: var(--orange); }
  .brand--aqua { color: var(--brand-deep); }
  .brand--well { color: var(--brand-sky); }

  /* Guide page */
  .guide__heading { position: absolute; left: 56px; top: 33px; width: 408px; height: 53px; border: 3px solid #fff; border-radius: 14px; background: var(--navy); color: #fff; font-family: "Roboto Condensed", sans-serif; font-size: 22px; display: flex; align-items: center; justify-content: center; }
  .guide__card { position: absolute; left: 30px; top: 108px; width: 468px; height: 460px; background: linear-gradient(#fff, #f3f3f4); border: 3px solid var(--sun); border-bottom: none; border-radius: 10px 10px 0 0; padding: 34px 20px 0 20px; font-family: "Open Sans", sans-serif; color: var(--ink); }
  .guide__warning { font-style: italic; font-size: 10.2px; line-height: 1.6; margin-bottom: 2px; }
  .guide__lead { font-style: italic; font-size: 10.5px; color: var(--brand-sky); margin: 16px 0 6px; }
  .guide__body { font-size: 7.6px; line-height: 1.48; text-align: justify; margin-bottom: 7px; }

  .guide__brand { position: absolute; left: 276px; top: 522px; color: var(--orange); font-size: 20px; }
  .guide__contact { position: absolute; left: 0; top: 620px; width: 522px; text-align: center; font-family: "Open Sans", sans-serif; font-size: 11.6px; color: var(--muted); line-height: 1.55; }
  .guide__bar { position: absolute; left: 30px; top: 672px; width: 460px; height: 37px; border-radius: 7px; background: var(--navy); display: flex; align-items: center; justify-content: space-between; padding: 0 9px; font-family: "Open Sans", sans-serif; font-size: 10.6px; color: #fff; }
  .guide__bar span { display: flex; align-items: center; gap: 4px; }
  .guide__bar svg { width: 10px; height: 10px; }
</style>
</head>
<body>
<main class="canvas">

  <section class="page page--cover" aria-label="Brochure cover">
    <div class="cover__sun"></div>
    <div class="cover__photo" role="img" aria-label="Photo of tilted solar panels against a blue sky with white clouds and green grass below"></div>
    <svg class="waves" viewBox="0 0 522 731" aria-hidden="true">
      <path d="M0,188 C130,150 250,205 380,205 C440,205 490,185 522,160 L522,0 L0,0 Z" fill="none"/>
      <path d="M0,232 C110,190 250,200 360,206 C440,210 490,195 522,178 L522,150 C470,175 420,185 350,182 C230,176 110,175 0,212 Z" fill="#ffffff"/>
      <path d="M0,268 C110,222 250,214 360,214 C440,214 490,200 522,186 L522,175 C480,196 420,206 350,204 C230,200 110,208 0,242 Z" fill="var(--navy)"/>
      <path d="M0,242 C110,208 230,200 350,204 C420,206 480,196 522,175 L522,186 C490,200 440,214 360,214 C250,214 110,222 0,268 Z" fill="var(--navy)"/>
      <path d="M0,580 C120,560 230,590 340,606 C420,616 480,600 522,560 L522,731 L0,731 Z" fill="var(--paper-shade)"/>
      <path d="M0,574 C120,554 230,584 340,600 C420,610 480,594 522,548 L522,560 C480,600 420,616 340,606 C230,590 120,560 0,580 Z" fill="var(--sun)"/>
      <path d="M0,560 C120,540 230,570 340,588 C420,598 480,580 522,520 L522,548 C480,594 420,610 340,600 C230,584 120,554 0,574 Z" fill="var(--brand-sky)"/>
      <path d="M522,470 C500,560 470,620 440,660 L470,660 C495,620 512,570 522,520 Z" fill="var(--brand-sky)"/>
    </svg>
    <h1 class="cover__title cover__title--sub">Submersible Pump</h1>
    <p class="cover__title cover__title--main">HOW TO GUIDES</p>
    <div class="brand-box">
      <span class="brand brand--sun"><span class="brand__dot"></span>Sunwellflow</span>
      <span class="brand brand--aqua">Aquadeepflow Depot</span>
      <span class="brand brand--well"><span class="brand__dot"></span>Wellflowy</span>
    </div>
  </section>

  <section class="page page--guide" aria-label="Fault finding guide">
    <h2 class="guide__heading">8. Submersible Pump Fault Finding Guide</h2>
    <article class="guide__card">
      <p class="guide__warning">Electricity will kill you if you contact live wires or components. Ensure the power supply is isolated from the pump, controls and switches before carrying out repairs.</p>
      <p class="guide__warning">A pump that is not working may still be live. Fault finding and repairs must be carried out by a trained and skilled operator.</p>
      <p class="guide__lead">Is pump working? If yes - leave it alone.</p>
      <p class="guide__body">No - Is power available? If the circuit breaker has tripped try resetting it. Sometimes a power supply fluctuation might cause a nuisance trip. If it trips again a short or overload condition is present. Isolate power supply and check with the multimeter to ensure it is safe. Disconnect the pump drop cable from junction box, pressure switch or pump controller and reset circuit breaker. If the circuit breaker trips again the fault is above ground in a cable, switch or controller.</p>
      <p class="guide__body">If circuit breaker didn't trip again with pump disconnected. The fault is below ground. The next test may be to Megga the drop cable and motor with Megg Ohm meter. A measurement of a low resistance of the motor windings to earth will indicate the fault in the drop cable, pump or motor. The pump will need to be removed and tests carried out on the motor and cable separately.</p>
      <p class="guide__body">Yes - Power available. Has the pump controller or protection device tripped out? Follow the instructions for that type of device. It may have saved the pump and motor from damage, the fault may not be present now and pumping may return to normal. If a protection device is not used external switches like a pressure switch, flow switch or level switch may have not allowed the pump to start. Check the power into and out of the switches. These switches may be temporarily by-passed to test the pump.</p>
      <p class="guide__body">If power is available to the pump via the drop cable—is the water pressure increasing or can water flow be heard? A blocked filter or damaged valve may be stopping water flow from the pump. If power is available and water flow or pressure can not be found the next step is to pull the pump and motor from the bore. The motor may be open circuit, the pump may have failed, the drop cable may be open circuit or the pump and motor may be operating and all the pumped water may be leaking from a hole in the pump column.</p>
    </article>
    <svg class="waves" viewBox="0 0 522 731" aria-hidden="true">
      <path d="M0,552 C120,530 230,570 330,586 C420,598 480,585 522,560 L522,731 L0,731 Z" fill="var(--paper-shade)"/>
      <path d="M0,534 C120,520 230,560 330,574 C420,586 480,574 522,546 L522,560 C480,585 420,598 330,586 C230,570 120,530 0,552 Z" fill="var(--navy)"/>
      <path d="M0,530 C120,516 230,556 330,570 C420,582 480,566 522,530 L522,546 C480,574 420,586 330,574 C230,560 120,520 0,534 Z" fill="var(--sun)"/>
    </svg>
    <span class="brand guide__brand"><span class="brand__dot"></span>Sunwellflow</span>
    <p class="guide__contact">If you need assistance call 1300 555 018 or mobile 0400 555 274<br>Email: info@aquadeepflow.com.au</p>
    <footer class="guide__bar">
      <span><svg viewBox="0 0 10 10"><circle cx="5" cy="5" r="4" fill="none" stroke="#fff" stroke-width="1.2"/><path d="M1,5 H9 M5,1 C2.5,3.5 2.5,6.5 5,9 M5,1 C7.5,3.5 7.5,6.5 5,9" fill="none" stroke="#fff" stroke-width=".8"/></svg>www.sunwellflow.com.au</span>
      <span><svg viewBox="0 0 10 10"><path d="M2,1 L4,1 L4.6,3 L3.5,4 C4,5.3 4.8,6.1 6,6.6 L7,5.5 L9,6.1 L9,8 C9,8.6 8.5,9 8,9 C4.5,8.7 1.3,5.5 1,2 C1,1.5 1.4,1 2,1 Z" fill="#fff"/></svg>1300 555 018</span>
      <span><svg viewBox="0 0 10 10"><circle cx="5" cy="5" r="4" fill="none" stroke="#fff" stroke-width="1.2"/><path d="M1,5 H9 M5,1 C2.5,3.5 2.5,6.5 5,9 M5,1 C7.5,3.5 7.5,6.5 5,9" fill="none" stroke="#fff" stroke-width=".8"/></svg>www.aquadeepflow.com.au</span>
    </footer>
  </section>

</main>
</body>
</html>
```